Verdane Kiwi Root Essence Prime Serum - Product Label

Hi Guys,

I threw up a rough label sketch. Looking to keep the label clean and fresh.

LABEL DIMENSIONS: 4.05 in (Height) x 1.18 in (Diameter)

Industry/Entity Type

Beauty Aid

Font styles to use
Serif

Colors
0255a3
0592cd
6b449b
ffc214

Requirements
Must have
• Lumivelle
• __________
• S K I N
Nice to have
• We can try purple, gold and black or stick with the blue scheme we have going.

```html
<!DOCTYPE html>
<html lang="en">
<head>
<meta charset="utf-8">
<title>Verdane Kiwi Root Essence Prime Serum – Label</title>
<link rel="stylesheet" href="https://fonts.googleapis.com/css2?family=Abel&family=Forum&family=Dosis:wght@400;600&display=swap">
<style>
  :root {
    --bg: #f2f2f2;
    --label: #ffffff;
    --ink-blue: #1f5c9c;
    --brand-ink: #1d1d1f;
    --band-top: #2a8bcb;
    --band-mid: #6fb1dd;
    --band-end: #ffffff;
    --band-text: #ffffff;
    --volume-text: #1f5c9c;
    --badge-pink: #f08cb8;
    --badge-grey: #c9ccd1;
    --badge-blue: #1f5fae;
  }
  * { box-sizing: border-box; margin: 0; padding: 0; }
  html, body { width: 1200px; height: 678px; overflow: hidden; }
  body {
    background: var(--bg);
    position: relative;
    font-family: "Abel", sans-serif;
  }
  .label {
    position: absolute;
    left: 72px; top: 103px;
    width: 1055px; height: 471px;
    background: var(--label);
    border-radius: 8px;
    box-shadow: 6px 8px 10px rgba(0,0,0,0.25);
  }
  .info-column {
    position: absolute;
    left: 19px; top: 26px;
    width: 290px;
    color: var(--ink-blue);
    font-size: 19px;
    line-height: 24.2px;
  }
  .info-column .directions { margin-top: 24px; }
  .brand-name {
    position: absolute;
    left: 346px; top: 206px;
    width: 364px;
    text-align: center;
    font-family: "Forum", serif;
    font-size: 44px;
    letter-spacing: 7px;
    color: var(--brand-ink);
    line-height: 1;
  }
  .product-band {
    position: absolute;
    left: 346px; top: 264px;
    width: 364px; height: 207px;
    background: linear-gradient(180deg, var(--band-top) 0%, var(--band-mid) 45%, var(--band-end) 100%);
    text-align: center;
  }
  .product-title {
    margin-top: 6px;
    font-family: "Dosis", sans-serif;
    font-weight: 400;
    font-size: 27px;
    line-height: 32px;
    letter-spacing: 2px;
    color: var(--band-text);
  }
  .product-title strong { font-weight: 600; letter-spacing: 3px; }
  .volume {
    position: absolute;
    left: 0; right: 0; top: 152px;
    font-size: 19px;
    color: var(--volume-text);
  }
  .distributor {
    position: absolute;
    left: 779px; top: 70px;
    width: 240px;
    text-align: center;
    color: var(--ink-blue);
    font-size: 19px;
    line-height: 24.2px;
  }
  .badges {
    position: absolute;
    left: 772px; top: 250px;
    display: flex;
    gap: 26px;
    align-items: center;
  }
</style>
</head>
<body>
  <main class="label">
    <section class="info-column">
      <p class="ingredients">Ingredient List: Purified Water, (VitaCellPro Stem Cell) Actinidia Deliciosa, Glycerin, Lecithin, Phenoxyethanol Collagen, Palmitoyl Tetrapeptide-3, (PeptiFirm 3000), Propylene Glycol, Polyglutamic Acid, Phenoxyetanol, Hydroxyethylcellulose, Propylene Glycol, Benzylalcohol, Dehydroacetic Acid</p>
      <p class="directions">How to Use: Wash area where you will apply the Kiwi Root Essence Serum thoroughly. Apply the product and let absorb for 15 minutes then apply moisturizer if desire.</p>
    </section>

    <h1 class="brand-name">LUMIVELLE</h1>

    <section class="product-band">
      <h2 class="product-title">VERDANE KIWI ROOT<br>ESSENCE PRIME<br><strong>SERUM</strong></h2>
      <p class="volume">1 fl. oz / 30ml</p>
    </section>

    <section class="distributor">
      <p>Distributed by Lumivelle</p>
      <p>Address</p>
      <p>Website</p>
    </section>

    <section class="badges" aria-label="Certification marks">
      <svg width="70" height="76" viewBox="0 0 70 76" role="img" aria-label="Cruelty free badge">
        <circle cx="35" cy="38" r="30" fill="var(--badge-pink)" opacity="0.35"/>
      </svg>
      <svg width="64" height="70" viewBox="0 0 64 70" role="img" aria-label="Period after opening badge">
        <rect x="6" y="16" width="52" height="42" rx="6" fill="none" stroke="var(--brand-ink)" stroke-width="2"/>
      </svg>
      <svg width="66" height="66" viewBox="0 0 66 66" role="img" aria-label="Manufacturing practice badge">
        <circle cx="33" cy="33" r="31" fill="var(--badge-blue)"/>
      </svg>
    </section>
  </main>
</body>
</html>
```